Personal contact Business card design needed

I work in the Property Industry - specifically Property Management.

I need a card I can hand out to colleagues at networking events, meetings, training courses etc. that will provide my contact details.

Target Market(s)

Professional colleagues / potential clients / employers

Industry/Entity Type

Training

Contact Information for Business Card

I need a simple and professional card to give to professional network contacts at meetings, interviews etc.

The card should include my photograph, name, mobile number, email address and Careerloom address.

I would like appropriate professional colours. Something feminine but not too 'frilly' or 'girly'

Requirements
Must have
• Photograph of myself.
I want it to be simple,perhaps a small icon for each contact detail such as
Email icon
Careerloom icon
Mobile number

```html
<!DOCTYPE html>
<html lang="en">
<head>
<meta charset="utf-8">
<title>Property Management – Business Card</title>
<link rel="stylesheet" href="https://fonts.googleapis.com/css2?family=Poiret+One&family=Libre+Baskerville:wght@700&display=swap">
<style>
  :root {
    --page-bg: #ecebee;
    --card-white: #ffffff;
    --ink: #1b1b1b;
    --purple: #8e3f8f;
    --purple-light: #b57ab6;
    --purple-dark: #5e2160;
    --curve-line: #3a3a3a;
    --ghost: #ececef;
  }
  * { box-sizing: border-box; margin: 0; padding: 0; }
  html, body {
    width: 1200px; height: 675px; overflow: hidden;
    background: var(--page-bg);
  }
  .card {
    position: absolute; left: 60px; top: 29px;
    width: 1080px; height: 617px;
    background: var(--card-white);
    overflow: hidden;
    box-shadow: 0 6px 18px rgba(0,0,0,0.18);
  }
  .backdrop-scene {
    position: absolute; left: 300px; top: 90px; width: 520px; height: 420px;
    border-radius: 50%;
    background: radial-gradient(ellipse at center, var(--ghost) 0%, rgba(236,236,239,0.6) 45%, rgba(255,255,255,0) 72%);
  }
  .band { position: absolute; inset: 0; width: 100%; height: 100%; }
  .title {
    position: absolute;
    font-family: "Poiret One", sans-serif;
    text-transform: uppercase;
    letter-spacing: 1px;
    line-height: 1;
    font-weight: 400;
  }
  .title-property {
    left: 300px; top: 48px; font-size: 72px; color: var(--ink);
    text-shadow: 2px 2px 2px rgba(0,0,0,0.25);
    -webkit-text-stroke: 1.5px var(--ink);
  }
  .title-management {
    left: 440px; top: 112px; font-size: 80px; color: var(--purple);
    text-shadow: 3px 3px 3px rgba(0,0,0,0.3);
    -webkit-text-stroke: 1.5px var(--purple);
  }
  .detail {
    position: absolute;
    font-family: "Libre Baskerville", serif;
    font-weight: 700;
    font-size: 19px;
    color: var(--ink);
    display: flex; align-items: center; gap: 10px;
    white-space: nowrap;
  }
  .detail-name { left: 110px; top: 222px; }
  .detail-phone { left: 110px; top: 262px; }
  .detail-email { left: 545px; top: 268px; }
  .detail-network { left: 535px; top: 328px; }
  .icon { width: 40px; height: 40px; flex: none; }
  .network-mark {
    width: 34px; height: 34px; border-radius: 4px;
    background: var(--purple); flex: none;
    box-shadow: 2px 2px 2px rgba(0,0,0,0.3);
  }
  .portrait {
    position: absolute; left: 330px; top: 330px; width: 200px; height: 200px;
    border-radius: 90px 90px 0 0;
    background: linear-gradient(180deg, #4a2a22 0%, #7a5345 40%, #1e1a1c 100%);
  }
</style>
</head>
<body>
  <main class="card">
    <div class="backdrop-scene" role="img" aria-label="Faint background photo of a house front"></div>

    <svg class="band" viewBox="0 0 1080 617" aria-hidden="true">
      <defs>
        <linearGradient id="bandFill" x1="0" y1="0" x2="0" y2="1">
          <stop offset="0" stop-color="var(--purple-light)"/>
          <stop offset="0.5" stop-color="var(--purple)"/>
          <stop offset="1" stop-color="var(--purple-dark)"/>
        </linearGradient>
      </defs>
      <path d="M0,345 Q420,620 1080,470 L1080,617 L0,617 Z" fill="url(#bandFill)"/>
      <path d="M0,345 Q420,620 1080,470" fill="none" stroke="var(--curve-line)" stroke-width="5"/>
    </svg>

    <div class="portrait" role="img" aria-label="Portrait photograph of the card holder"></div>

    <h1 class="title title-property">Property</h1>
    <h2 class="title title-management">Management</h2>

    <p class="detail detail-name">Name: Dana Whitmore</p>

    <p class="detail detail-phone">
      <svg class="icon" viewBox="0 0 40 40" aria-hidden="true">
        <rect x="4" y="11" width="32" height="18" rx="3" transform="rotate(-20 20 20)" fill="var(--purple)"/>
        <rect x="9" y="15" width="20" height="10" rx="1" transform="rotate(-20 20 20)" fill="var(--purple-light)"/>
      </svg>
      <span>: 0400 555 123</span>
    </p>

    <p class="detail detail-email">
      <svg class="icon" viewBox="0 0 40 40" aria-hidden="true">
        <rect x="5" y="9" width="30" height="22" fill="none" stroke="var(--purple)" stroke-width="3"/>
        <path d="M5,9 L20,22 L35,9" fill="none" stroke="var(--purple)" stroke-width="3"/>
      </svg>
      <span>: dana@mailbox-example.com.au</span>
    </p>

    <p class="detail detail-network">
      <span class="network-mark" aria-hidden="true"></span>
      <span>: careerloom.com/in/danawhitmore</span>
    </p>
  </main>
</body>
</html>
```